Carwash Signage

We own and operate a 25m tunnel car wash in the uk. We are looking to upgrade our signage to include the following:-

Wash selection Board Size-1300x1300mm
Conditions 1300x1300mm
Instructions 1300x1300mm
Banner 2600x600mm
Stamp card flyer a5 double sided - 9 squares for stamping 3rd square needs to say free air freshener 9th square needs to say free vip car wash.

I have attached some notes for the details that are required to be included.

We are looking for a modern smart look more European car wash style than American car wash style. It should be bold and clear. with yellow/orange & blue/green,grey colours

The final design must be in a industry standard printable format.

UPDATED BRIEF AS DISCUSSED: We require design for 2 x window decals, flag design and 50% off voucher. Attached are rough layout drawings of what they should look like - we expect the designs to be in keeping with the previous designs colours, etc that have been carried out. We Look forward to hearing from you.

Target Market(s)

local car owners within a 15-20 mile radius

Colors
0054AA
0677BA
7BADD7
CADEEF
E8F1F8
0094D4
00A9DD
6FCCEA
C7EBF8
E9F6FB
00AB8E
00BBA5
67D7C9
C6EFE9
E9F9F6

Requirements
Must have
• must be sharp and modern European look

```html
<!DOCTYPE html>
<html lang="nl">
<head>
<meta charset="utf-8">
<title>Brightway Car Wash – A5 flyer</title>
<link rel="stylesheet" href="https://fonts.googleapis.com/css2?family=Montserrat:wght@700;800&family=Lexend:wght@400;500;600&display=swap">
<style>
:root{
  --board:#b9b9b9;
  --ink:#1b1b1b;
  --white:#ffffff;
  --blue:#1539d4;
  --blue-mid:#0f2fb8;
  --blue-deep:#0a2384;
  --navy:#1a2160;
  --sky:#00A9DD;
  --sky-soft:#3fcbec;
  --ocean:#0677BA;
  --teal:#00BBA5;
  --teal-deep:#00AB8E;
  --orange:#ff7a1f;
  --orange-deep:#f2601a;
}
*{box-sizing:border-box;margin:0;padding:0}
html,body{width:1200px;height:851px;overflow:hidden}
body{background:var(--board);font-family:"Lexend",sans-serif;position:relative;color:var(--white)}

/* print measurements */
.measure{position:absolute;color:var(--ink);font-family:"Lexend",sans-serif;font-size:14px}
.measure-width{left:80px;top:34px;width:502px;display:flex;align-items:center;gap:8px}
.measure-width .rule{flex:1;border-top:1px dashed var(--ink)}
.measure-height{left:48px;top:74px;height:712px;width:20px;display:flex;flex-direction:column;align-items:center;gap:8px}
.measure-height .rule{flex:1;border-left:1px dashed var(--ink)}
.measure-height .label{writing-mode:vertical-rl;transform:rotate(180deg);white-space:nowrap}

/* flyer page */
.flyer{position:absolute;top:74px;width:502px;height:712px;overflow:hidden;
  background:radial-gradient(ellipse 80% 55% at 55% 40%,#2250ea 0%,var(--blue) 45%,var(--blue-mid) 75%,var(--blue-deep) 100%);
  box-shadow:0 14px 30px rgba(0,0,0,.25)}
.flyer-front{left:80px}
.flyer-back{left:619px}
.flyer svg.shapes{position:absolute;inset:0}

.brand{position:absolute;top:24px;left:0;width:502px;display:flex;justify-content:center;align-items:flex-end;gap:8px;color:var(--navy)}
.brand-dot{width:30px;height:30px;border-radius:50%;background:var(--navy);margin-bottom:4px}
.brand-words{display:flex;flex-direction:column;align-items:flex-end;font-family:"Montserrat",sans-serif;font-weight:800}
.brand-tag{font-size:12px;letter-spacing:3px;line-height:1}
.brand-name{font-size:36px;line-height:1.05;letter-spacing:.5px}

/* front */
.kicker{position:absolute;top:108px;width:100%;text-align:center;font-family:"Lexend",sans-serif;font-weight:600;font-size:25px;color:var(--sky-soft)}
.hero-title{position:absolute;top:136px;width:100%;text-align:center;font-family:"Montserrat",sans-serif;font-weight:800;font-size:70px;letter-spacing:-2px;line-height:1}
.payments{position:absolute;top:207px;width:100%;text-align:center;font-family:"Montserrat",sans-serif;font-weight:700;font-size:12px;letter-spacing:3px}

.hours-band{position:absolute;top:244px;left:0;width:290px;height:27px;background:linear-gradient(90deg,var(--sky) 0%,var(--sky) 70%,rgba(0,169,221,0) 100%);
  font-family:"Montserrat",sans-serif;font-weight:800;font-size:18px;line-height:27px;padding-left:38px}
.hours{position:absolute;top:278px;left:38px;font-size:16px;line-height:22px}
.hours p + p{margin-top:0}
.hours .gap{margin-top:2px}

.car-photo{position:absolute;left:226px;top:222px;width:276px;height:280px;
  background:radial-gradient(ellipse 60% 40% at 60% 60%,#eef2f7 0%,#c9d3e2 40%,rgba(120,170,230,.6) 70%,rgba(21,57,212,0) 100%)}

.perks{position:absolute;top:383px;left:38px;list-style:none;font-size:13px;line-height:21px}
.perks li{display:flex;align-items:center;gap:8px;white-space:nowrap}
.perks li.cont{padding-left:21px}
.tick{width:13px;height:13px;flex:none}

.footer-title{position:absolute;top:613px;width:100%;text-align:center;font-family:"Montserrat",sans-serif;font-weight:800;font-size:22px}
.footer-address{position:absolute;top:643px;width:100%;text-align:center;font-size:13px}
.call-band{position:absolute;left:0;bottom:0;width:285px;height:42px;background:var(--sky);clip-path:polygon(0 0,265px 0,285px 100%,0 100%);
  display:flex;align-items:center;gap:6px;padding-left:38px;font-weight:500;font-size:20px}
.call-band svg{width:16px;height:16px}
.contact{position:absolute;left:297px;top:670px;font-size:14px;font-weight:500;line-height:17px}

/* back */
.back-title{position:absolute;top:118px;width:100%;text-align:center;font-family:"Montserrat",sans-serif;font-weight:800;font-size:20px;line-height:25px}
.stamp{position:absolute;width:127px;height:130px;background:var(--white);outline:2px dotted var(--white);outline-offset:2px;color:var(--navy)}
.stamp .mini-brand{position:absolute;top:8px;left:0;width:100%;display:flex;justify-content:center;align-items:flex-end;gap:3px}
.mini-brand .brand-dot{width:9px;height:9px;margin-bottom:2px}
.mini-brand .brand-tag{font-size:4px;letter-spacing:1px}
.mini-brand .brand-name{font-size:11px}
.stamp .deal{position:absolute;top:31px;left:8px;width:111px;height:80px;padding:8px 0 0 8px;color:var(--white)}
.deal h3{font-family:"Montserrat",sans-serif;font-weight:800;font-size:15px;line-height:18px}
.deal p{font-size:5.5px;line-height:9px;margin-top:4px}
.deal-teal{background:var(--teal)}
.deal-ocean{background:var(--ocean)}
.deal-sky{background:var(--sky)}
.price{position:absolute;right:-2px;bottom:-8px;width:32px;height:32px;border-radius:50%;background:var(--orange);border:2px solid var(--white);
  display:flex;flex-direction:column;align-items:center;justify-content:center;font-family:"Montserrat",sans-serif;font-weight:800;line-height:1}
.price s{font-size:6px}
.price b{font-size:12px}
.price .free{font-size:9px}
.stamp .expiry{position:absolute;left:8px;bottom:5px;font-size:6.5px}
</style>
</head>
<body>

<div class="measure measure-width"><span class="rule"></span><span>148 mm + 3 mm bleed</span><span class="rule"></span></div>
<div class="measure measure-height"><span class="rule"></span><span class="label">210 mm + 3 mm bleed</span><span class="rule"></span></div>

<!-- Front side -->
<section class="flyer flyer-front">
  <svg class="shapes" viewBox="0 0 502 712" aria-hidden="true">
    <path d="M0 0H502V36Q251 158 0 36Z" fill="#fff"/>
    <path d="M0 600C150 620 350 615 502 580V712H0Z" fill="#0a2384" opacity=".6"/>
    <path d="M0 515C120 560 300 585 502 505L502 532C330 612 130 612 0 560Z" fill="#ff7a1f"/>
    <path d="M120 600C250 610 380 595 502 560L502 570C380 610 250 620 120 606Z" fill="#f2601a"/>
  </svg>

  <div class="brand">
    <span class="brand-dot"></span>
    <div class="brand-words"><span class="brand-tag">CAR WASH</span><span class="brand-name">BRIGHTWAY</span></div>
  </div>

  <p class="kicker">9x korting op een schone auto!</p>
  <h1 class="hero-title">CAR WASH</h1>
  <p class="payments">CASH + CARD PAYMENTS ACCEPTED</p>

  <div class="car-photo" role="img" aria-label="Photo of a white SUV surrounded by splashing water"></div>

  <h2 class="hours-band">OPENINGSTIJDEN</h2>
  <div class="hours">
    <p>Maandag t/m zaterdag:</p>
    <p>08:30 - 18:00 uur</p>
    <p class="gap">Zon-en feestdagen:</p>
    <p>9:00 - 16:00 uur</p>
  </div>

  <ul class="perks">
    <li><svg class="tick" viewBox="0 0 14 14"><circle cx="7" cy="7" r="7" fill="#00BBA5"/><path d="M5 9L9.5 4.5M6 4.5H9.5V8" stroke="#0f2fb8" stroke-width="1.4" fill="none"/></svg>Gatis indoor stofzuigen</li>
    <li><svg class="tick" viewBox="0 0 14 14"><circle cx="7" cy="7" r="7" fill="#00BBA5"/><path d="M5 9L9.5 4.5M6 4.5H9.5V8" stroke="#0f2fb8" stroke-width="1.4" fill="none"/></svg>Gratis banden pompen</li>
    <li><svg class="tick" viewBox="0 0 14 14"><circle cx="7" cy="7" r="7" fill="#00BBA5"/><path d="M5 9L9.5 4.5M6 4.5H9.5V8" stroke="#0f2fb8" stroke-width="1.4" fill="none"/></svg>Superffectieve mattenwasser</li>
    <li><svg class="tick" viewBox="0 0 14 14"><circle cx="7" cy="7" r="7" fill="#00BBA5"/><path d="M5 9L9.5 4.5M6 4.5H9.5V8" stroke="#0f2fb8" stroke-width="1.4" fill="none"/></svg>Krasvrij wassen</li>
    <li><svg class="tick" viewBox="0 0 14 14"><circle cx="7" cy="7" r="7" fill="#00BBA5"/><path d="M5 9L9.5 4.5M6 4.5H9.5V8" stroke="#0f2fb8" stroke-width="1.4" fill="none"/></svg>Velgen reiniging</li>
    <li><svg class="tick" viewBox="0 0 14 14"><circle cx="7" cy="7" r="7" fill="#00BBA5"/><path d="M5 9L9.5 4.5M6 4.5H9.5V8" stroke="#0f2fb8" stroke-width="1.4" fill="none"/></svg>Ook geschikt voor bedrijfswagens</li>
    <li class="cont">tot max. 2,05m hoog (zonder imperial)</li>
  </ul>

  <h2 class="footer-title">EXPERT TEAM CAR WASHING</h2>
  <p class="footer-address">Molenweg 12, 6211 AB, Dorpstad</p>
  <div class="call-band">Call <svg viewBox="0 0 24 24"><path fill="#fff" d="M6.6 10.8a15 15 0 0 0 6.6 6.6l2.2-2.2a1 1 0 0 1 1-.25 11.4 11.4 0 0 0 3.6.57 1 1 0 0 1 1 1V20a1 1 0 0 1-1 1A17 17 0 0 1 3 4a1 1 0 0 1 1-1h3.5a1 1 0 0 1 1 1c0 1.25.2 2.45.57 3.57a1 1 0 0 1-.25 1Z"/></svg>123 456 7890</div>
  <div class="contact"><p>info@websiteurl.com</p><p>www.websiteurl.com</p></div>
</section>

<!-- Back side: stamp card -->
<section class="flyer flyer-back">
  <svg class="shapes" viewBox="0 0 502 712" aria-hidden="true">
    <path d="M0 0H502V36Q251 158 0 36Z" fill="#fff"/>
    <path d="M0 600C150 620 350 615 502 580V712H0Z" fill="#0a2384" opacity=".6"/>
    <path d="M0 493C150 520 350 512 502 465L502 500C350 560 150 562 0 540Z" fill="#ff7a1f"/>
  </svg>

  <div class="brand">
    <span class="brand-dot"></span>
    <div class="brand-words"><span class="brand-tag">CAR WASH</span><span class="brand-name">BRIGHTWAY</span></div>
  </div>

  <h1 class="back-title">UNLOCK A FREE CAR WASH WITH<br>A COMPLETED STAMP CARD</h1>

  <div class="stamp" style="left:41px;top:183px">
    <div class="mini-brand"><span class="brand-dot"></span><div class="brand-words"><span class="brand-tag">CAR WASH</span><span class="brand-name">BRIGHTWAY</span></div></div>
    <div class="deal deal-teal"><h3>REGULAR<br>CAR WASH</h3><p>Lorem ipsum dolor sit<br>amet dummy texts</p><span class="price"><s>€16</s><b>€12</b></span></div>
    <p class="expiry">Offer till 20 Sept. 2025</p>
  </div>
  <div class="stamp" style="left:187px;top:183px">
    <div class="mini-brand"><span class="brand-dot"></span><div class="brand-words"><span class="brand-tag">CAR WASH</span><span class="brand-name">BRIGHTWAY</span></div></div>
    <div class="deal deal-ocean"><h3>REGULAR<br>CAR WASH</h3><p>Lorem ipsum dolor sit<br>amet dummy texts</p><span class="price"><s>€16</s><b>€12</b></span></div>
    <p class="expiry">Offer till 20 Sept. 2025</p>
  </div>
  <div class="stamp" style="left:334px;top:183px">
    <div class="mini-brand"><span class="brand-dot"></span><div class="brand-words"><span class="brand-tag">CAR WASH</span><span class="brand-name">BRIGHTWAY</span></div></div>
    <div class="deal deal-sky"><h3>AIR<br>FRESHENER</h3><p>Lorem ipsum dolor sit<br>amet dummy texts</p><span class="price"><b class="free">FREE</b></span></div>
    <p class="expiry">Offer till 20 Sept. 2025</p>
  </div>

  <div class="stamp" style="left:41px;top:326px">
    <div class="mini-brand"><span class="brand-dot"></span><div class="brand-words"><span class="brand-tag">CAR WASH</span><span class="brand-name">BRIGHTWAY</span></div></div>
    <div class="deal deal-ocean"><h3>REGULAR<br>CAR WASH</h3><p>Lorem ipsum dolor sit<br>amet dummy texts</p><span class="price"><s>€16</s><b>€12</b></span></div>
    <p class="expiry">Offer till 20 Sept. 2025</p>
  </div>
  <div class="stamp" style="left:187px;top:326px">
    <div class="mini-brand"><span class="brand-dot"></span><div class="brand-words"><span class="brand-tag">CAR WASH</span><span class="brand-name">BRIGHTWAY</span></div></div>
    <div class="deal deal-teal"><h3>REGULAR<br>CAR WASH</h3><p>Lorem ipsum dolor sit<br>amet dummy texts</p><span class="price"><s>€16</s><b>€12</b></span></div>
    <p class="expiry">Offer till 20 Sept. 2025</p>
  </div>
  <div class="stamp" style="left:334px;top:326px">
    <div class="mini-brand"><span class="brand-dot"></span><div class="brand-words"><span class="brand-tag">CAR WASH</span><span class="brand-name">BRIGHTWAY</span></div></div>
    <div class="deal deal-ocean"><h3>REGULAR<br>CAR WASH</h3><p>Lorem ipsum dolor sit<br>amet dummy texts</p><span class="price"><s>€16</s><b>€12</b></span></div>
    <p class="expiry">Offer till 20 Sept. 2025</p>
  </div>

  <div class="stamp" style="left:41px;top:469px">
    <div class="mini-brand"><span class="brand-dot"></span><div class="brand-words"><span class="brand-tag">CAR WASH</span><span class="brand-name">BRIGHTWAY</span></div></div>
    <div class="deal deal-sky"><h3>REGULAR<br>CAR WASH</h3><p>Lorem ipsum dolor sit<br>amet dummy texts</p><span class="price"><s>€16</s><b>€12</b></span></div>
    <p class="expiry">Offer till 20 Sept. 2025</p>
  </div>
  <div class="stamp" style="left:187px;top:469px">
    <div class="mini-brand"><span class="brand-dot"></span><div class="brand-words"><span class="brand-tag">CAR WASH</span><span class="brand-name">BRIGHTWAY</span></div></div>
    <div class="deal deal-ocean"><h3>REGULAR<br>CAR WASH</h3><p>Lorem ipsum dolor sit<br>amet dummy texts</p><span class="price"><s>€16</s><b>€12</b></span></div>
    <p class="expiry">Offer till 20 Sept. 2025</p>
  </div>
  <div class="stamp" style="left:334px;top:469px">
    <div class="mini-brand"><span class="brand-dot"></span><div class="brand-words"><span class="brand-tag">CAR WASH</span><span class="brand-name">BRIGHTWAY</span></div></div>
    <div class="deal deal-teal"><h3>VIP CAR<br>WASH</h3><p>Lorem ipsum dolor sit<br>amet dummy texts</p><span class="price"><b class="free">FREE</b></span></div>
    <p class="expiry">Offer till 20 Sept. 2025</p>
  </div>

  <h2 class="footer-title">EXPERT TEAM CAR WASHING</h2>
  <p class="footer-address">Molenweg 12, 6211 AB, Dorpstad</p>
  <div class="call-band">Call <svg viewBox="0 0 24 24"><path fill="#fff" d="M6.6 10.8a15 15 0 0 0 6.6 6.6l2.2-2.2a1 1 0 0 1 1-.25 11.4 11.4 0 0 0 3.6.57 1 1 0 0 1 1 1V20a1 1 0 0 1-1 1A17 17 0 0 1 3 4a1 1 0 0 1 1-1h3.5a1 1 0 0 1 1 1c0 1.25.2 2.45.57 3.57a1 1 0 0 1-.25 1Z"/></svg>123 456 7890</div>
  <div class="contact"><p>info@websiteurl.com</p><p>www.websiteurl.com</p></div>
</section>

</body>
</html>
```